Website for our 3rd party logistics warehouse company

Our company is a 3rd party logistics company. We receive and ship other businesses products for them. We offer our services to other smaller businesses that do not have a warehouse to operate out of. We also help many Brindlemart businesses prepare their products to be sold on Brindlemart.

We are looking for a modern looking design for our website. Please see our attached logo for design ideas. We are open to changing logo colors for website.

We really like the look of the website www.quorvela.com

Target Market(s)

Other businesses and brands of products

Industry/Entity Type

Warehousing and shipping

Number of Pages Required

2 page

Requirements
Must have
• We need 2 pages. Our main landing page and a duplicate page with different information geared towards brands.
Nice to have
• I like the look of overlay/transparent sections. Please see quorvela.com there is a ribbon that shows "Partners".

```html
<!DOCTYPE html>
<html lang="en">
<head>
<meta charset="utf-8">
<title>Keelstone 3PL – 3rd Party Logistics</title>
<link href="https://fonts.googleapis.com/css2?family=Raleway:wght@400;500;600;700&family=Roboto+Slab:wght@800;900&display=swap" rel="stylesheet">
<style>
:root{
  --gold:#e29e0c;
  --gold-dark:#c98a05;
  --ink:#1f1f1f;
  --text:#3d3d3d;
  --muted:#555;
  --nav:#2e2e30;
  --black:#0c0c0c;
  --light:#f2f2f2;
  --slate:#454a55;
  --footer:#2f3036;
  --white:#fff;
}
*{box-sizing:border-box;margin:0;padding:0}
html,body{width:1200px;height:3807px;overflow:hidden}
body{font-family:"Raleway",sans-serif;color:var(--text);background:var(--white);position:relative}
section,header,footer{position:absolute;left:0;width:1200px}
.slab{font-family:"Roboto Slab",serif;font-weight:900;color:var(--ink);letter-spacing:.5px}
.btn{display:inline-block;background:var(--gold);color:var(--white);font-weight:700;border-radius:30px;text-align:center;text-transform:uppercase}

/* header */
.site-header{top:0;height:126px;background:var(--nav)}
.brand-block{position:absolute;left:0;top:0;width:384px;height:126px;background:var(--black);clip-path:polygon(0 0,100% 0,86% 100%,0 100%)}
.brand{position:absolute;left:112px;top:46px;display:flex;align-items:center;gap:10px;font-weight:700;font-size:26px;color:var(--white);letter-spacing:2px}
.brand .dot{width:14px;height:14px;border-radius:50%;background:var(--gold)}
.call{position:absolute;right:110px;top:24px;color:var(--white);font-family:"Roboto Slab",serif;font-size:25px;display:flex;align-items:center;gap:8px}
.call b{font-weight:800}
.nav{position:absolute;right:90px;top:82px;display:flex;gap:32px;font-size:13.5px;font-weight:700;color:var(--white);text-transform:uppercase}
.nav .active{color:var(--gold);position:relative}
.nav .active::after{content:"";position:absolute;left:0;right:0;top:34px;height:3px;background:var(--gold)}

/* hero */
.hero{top:126px;height:601px;background:linear-gradient(160deg,#8d96a1 0%,#6f7984 45%,#5a4f4a 100%)}
.hero-photo{position:absolute;inset:0;background:radial-gradient(ellipse at 60% 40%,rgba(190,200,210,.35),transparent 60%)}
.hero h1{position:absolute;top:138px;width:100%;text-align:center;font-family:"Roboto Slab",serif;font-weight:900;font-size:66px;color:var(--white);letter-spacing:2px}
.hero p{position:absolute;top:214px;width:100%;text-align:center;font-size:21px;color:var(--white)}
.hero .btn{position:absolute;left:506px;top:264px;width:188px;height:48px;line-height:48px;font-size:14px}
.dots{position:absolute;top:570px;left:555px;display:flex;gap:9px}
.dots span{width:7px;height:7px;border-radius:50%;background:rgba(255,255,255,.6)}
.dots span:first-child{background:var(--gold)}

/* who */
.who{top:727px;height:488px}
.who h2{position:absolute;left:112px;top:104px;font-size:34px}
.who p{position:absolute;left:112px;top:160px;width:440px;font-size:19px;line-height:30px}
.who .btn{position:absolute;left:112px;top:340px;width:185px;height:52px;line-height:52px;font-size:17px}
.warehouse{position:absolute;left:628px;top:84px;width:461px;height:330px;border:4px solid var(--gold);background:linear-gradient(180deg,#5b8fd0 0%,#a9c8ea 38%,#dfe3e8 52%,#7c8085 70%,#62862f 100%)}

/* why */
.why{top:1215px;height:431px;background:var(--light)}
.why h2{position:absolute;top:60px;width:100%;text-align:center;font-size:32px}
.reason{position:absolute;top:150px;width:240px;text-align:center;font-size:14px;line-height:21px;color:var(--text)}
.reason .ring{width:128px;height:128px;border:2.5px solid var(--gold);border-radius:50%;margin:0 auto 14px;display:flex;align-items:center;justify-content:center}

/* benefits */
.benefits{top:1646px;height:422px;background:linear-gradient(180deg,#4b4f58 0%,#585c63 55%,#4a4644 100%)}
.benefits h2{position:absolute;top:68px;width:100%;text-align:center;font-size:36px;color:var(--white)}
.benefits ul{position:absolute;left:302px;top:135px;list-style:none;color:var(--white);font-size:21px;font-weight:500}
.benefits li{display:flex;align-items:center;gap:10px;height:38.5px}
.tick{width:18px;height:18px;background:var(--gold);border-radius:3px;display:flex;align-items:center;justify-content:center}

/* software */
.software{top:2068px;height:430px}
.devices{position:absolute;left:112px;top:82px;width:482px;height:266px;background:linear-gradient(180deg,#2f3136 0%,#d9dde3 10%,#eef0f3 85%,#b9bcc1 100%);border-radius:10px 10px 4px 4px}
.software h2{position:absolute;left:668px;top:90px;font-size:34px}
.software p{position:absolute;left:670px;top:152px;width:420px;font-size:19px;line-height:30px}

/* guarantee */
.guarantee{top:2498px;height:239px;background:var(--slate)}
.guarantee h2{position:absolute;top:52px;width:100%;text-align:center;font-size:35px;color:var(--white)}
.guarantee p{position:absolute;left:180px;top:112px;width:840px;text-align:center;font-size:17.5px;line-height:25px;color:var(--white)}
.guarantee strong{font-size:24px;font-weight:700}

/* contact */
.contact{top:2737px;height:562px;background:linear-gradient(180deg,#fafafa,#eef0f2)}
.contact h2{position:absolute;top:58px;width:100%;text-align:center;font-size:35px}
.contact .sub{position:absolute;top:118px;width:100%;text-align:center;font-size:18px}
.contact h3{position:absolute;left:112px;top:190px;font-size:26px;font-weight:600;color:var(--ink)}
.c-line{position:absolute;left:112px;font-size:19px;display:flex;align-items:center;gap:6px}
.form label{position:absolute;font-size:13.5px;color:var(--text)}
.field{position:absolute;background:var(--white);border:1px solid #b8b8b8}
.form .btn{position:absolute;left:535px;top:432px;width:200px;height:52px;line-height:52px;font-size:20px}

/* footer */
.site-footer{top:3299px;height:329px;background:var(--footer);color:var(--white)}
.f-brand{position:absolute;left:112px;top:76px;display:flex;align-items:center;gap:10px;font-size:27px;font-weight:700;letter-spacing:2px}
.f-brand .dot{width:14px;height:14px;border-radius:50%;background:var(--gold)}
.social{position:absolute;left:112px;top:190px;display:flex;gap:9px}
.social span{width:34px;height:34px;border-radius:50%;background:var(--gold)}
.site-footer h4{position:absolute;top:62px;font-size:16px;font-weight:700;text-transform:uppercase}
.f-links{position:absolute;top:108px;list-style:none;font-size:13px}
.f-links li{height:30px}
.f-contact{position:absolute;left:878px;top:108px;font-size:13px;line-height:22px}
.f-contact div{display:flex;gap:8px;margin-bottom:8px}
.rule{position:absolute;left:112px;right:112px;top:258px;height:1px;background:rgba(255,255,255,.12)}
.copy{position:absolute;top:280px;width:100%;text-align:center;font-size:12px}

/* disclaimer */
.disclaimer{top:3628px;height:179px;background:var(--gold);color:var(--white);text-align:center}
.disclaimer h5{margin-top:28px;font-size:26px;font-weight:600}
.disclaimer p{width:990px;margin:10px auto 0;font-size:11.5px;line-height:17px}
</style>
</head>
<body>

<header class="site-header">
  <div class="brand-block"></div>
  <div class="brand"><span class="dot"></span>KEELSTONE 3PL</div>
  <div class="call">
    <svg width="18" height="18" viewBox="0 0 24 24"><path fill="#fff" d="M6.6 10.8a15 15 0 0 0 6.6 6.6l2.2-2.2a1 1 0 0 1 1-.25 11.4 11.4 0 0 0 3.6.57 1 1 0 0 1 1 1V20a1 1 0 0 1-1 1A17 17 0 0 1 3 4a1 1 0 0 1 1-1h3.5a1 1 0 0 1 1 1c0 1.25.2 2.45.57 3.6a1 1 0 0 1-.25 1z"/></svg>
    CALL US NOW: <b>+1 (234) 567-8900</b>
  </div>
  <nav class="nav">
    <span class="active">Home</span><span>Who we are</span><span>Why use a prep 3PL?</span><span>Benefits</span><span>Our software</span><span>Contact us</span>
  </nav>
</header>

<section class="hero">
  <div class="hero-photo" role="img" aria-label="Container port with cargo ship and stacked containers overlaid with a connected world network map"></div>
  <h1>KEELSTONE 3PL</h1>
  <p>We are a 3rd party logistics company</p>
  <span class="btn">Request a quote</span>
  <div class="dots"><span></span><span></span><span></span><span></span><span></span><span></span></div>
</section>

<section class="who">
  <h2 class="slab">WHO WE ARE</h2>
  <p>Keelstone 3PL is your one stop 3PL that will help you grow your business and allow you to be hands off. We offer high end services and meet our commitment, guaranteed.</p>
  <span class="btn">Learn more</span>
  <div class="warehouse" role="img" aria-label="Modern warehouse building with trucks at loading docks under a blue sky"></div>
</section>

<section class="why">
  <h2 class="slab">WHY USE A PREP 3PL?</h2>
  <div class="reason" style="left:81px">
    <div class="ring"><svg width="70" height="70" viewBox="0 0 70 70" fill="none" stroke="#e29e0c" stroke-width="2.5"><path d="M8 32 35 10l27 22"/><path d="M16 26v34h38V26"/><circle cx="35" cy="34" r="7"/><rect x="26" y="46" width="20" height="10"/></svg></div>
    Work from anywhere in the world
  </div>
  <div class="reason" style="left:346px">
    <div class="ring"><svg width="70" height="70" viewBox="0 0 70 70" fill="none" stroke="#e29e0c" stroke-width="2.5"><circle cx="24" cy="16" r="6"/><path d="M14 58V34a10 10 0 0 1 20 0"/><path d="M38 24l14-6 14 6v12c0 10-7 17-14 20-7-3-14-10-14-20z"/><path d="M52 30v14M45 37h14"/></svg></div>
    Don't have to manage employees, health insurance plans, payroll, sick calls, etc.
  </div>
  <div class="reason" style="left:616px">
    <div class="ring"><svg width="70" height="70" viewBox="0 0 70 70" fill="none" stroke="#e29e0c" stroke-width="2.5"><path d="M8 24 35 10l27 14v36H8z"/><rect x="18" y="30" width="34" height="30"/><rect x="36" y="42" width="10" height="10"/><rect x="26" y="48" width="10" height="12"/></svg></div>
    Don't get locked into a 3-5 year warehouse lease where you guarantee hundreds of thousands of dollars
  </div>
  <div class="reason" style="left:879px">
    <div class="ring"><svg width="70" height="70" viewBox="0 0 70 70" fill="none" stroke="#e29e0c" stroke-width="2.5"><path d="M35 44V22"/><path d="M35 30c-10 0-14-8-14-12 8 0 14 4 14 12zM35 26c0-8 6-14 14-14 0 8-6 14-14 14z"/><path d="M8 50c8-4 14-4 22 0h12a4 4 0 0 1 0 8H26M44 54l14-8a4 4 0 0 1 4 6L46 62H8"/></svg></div>
    Grow your business without commitment
  </div>
</section>

<section class="benefits" role="img" aria-label="Background of cargo ship, container trucks and freight train under a city skyline">
  <h2 class="slab">OUR BENEFITS</h2>
  <ul>
    <li><span class="tick"><svg width="12" height="12" viewBox="0 0 12 12"><path d="M2 6l3 3 5-6" stroke="#fff" stroke-width="2" fill="none"/></svg></span>48 hour turn around guarantee – done in 48 hours or its free*</li>
    <li><span class="tick"><svg width="12" height="12" viewBox="0 0 12 12"><path d="M2 6l3 3 5-6" stroke="#fff" stroke-width="2" fill="none"/></svg></span>No monthly subscription – only pay for what you use</li>
    <li><span class="tick"><svg width="12" height="12" viewBox="0 0 12 12"><path d="M2 6l3 3 5-6" stroke="#fff" stroke-width="2" fill="none"/></svg></span>No receiving fees</li>
    <li><span class="tick"><svg width="12" height="12" viewBox="0 0 12 12"><path d="M2 6l3 3 5-6" stroke="#fff" stroke-width="2" fill="none"/></svg></span>No pallet or outbound fees</li>
    <li><span class="tick"><svg width="12" height="12" viewBox="0 0 12 12"><path d="M2 6l3 3 5-6" stroke="#fff" stroke-width="2" fill="none"/></svg></span>Email and phone support</li>
  </ul>
</section>

<section class="software">
  <div class="devices" role="img" aria-label="Laptop and phone showing the inventory tracking software dashboard"></div>
  <h2 class="slab">OUR SOFTWARE</h2>
  <p>Know what inventory is at our warehouse in real time. Our software allows you to track your inventory and know how your shipment status in real time. Professional software designed specifically for our needs.</p>
</section>

<section class="guarantee">
  <h2 class="slab">OUR GUARANTEE</h2>
  <p>All orders will be prepped and ready for shipment in 48 business hours (often 24 or less) and we guarantee it. We are confident in our services and if we do not fulfill our obligation, we offer a 500 item <strong>(up to $700)</strong> credit on your next shipment</p>
</section>

<section class="contact">
  <h2 class="slab">CONTACT US</h2>
  <div class="sub">Get Weekly Insights Into All Things Freight</div>
  <h3>Contact Us</h3>
  <div class="c-line" style="top:246px"><svg width="16" height="16" viewBox="0 0 16 16"><rect width="16" height="16" rx="3" fill="#e29e0c"/><path fill="#fff" d="M5 4l2 2-1 1a6 6 0 0 0 3 3l1-1 2 2-1.5 1.5C7 12 4 9 3.5 5.5z"/></svg>Tel. +1 (234) 567-8900</div>
  <div class="c-line" style="top:296px"><svg width="16" height="16" viewBox="0 0 24 24"><path fill="#e29e0c" d="M6.6 10.8a15 15 0 0 0 6.6 6.6l2.2-2.2a1 1 0 0 1 1-.25 11.4 11.4 0 0 0 3.6.57 1 1 0 0 1 1 1V20a1 1 0 0 1-1 1A17 17 0 0 1 3 4a1 1 0 0 1 1-1h3.5a1 1 0 0 1 1 1c0 1.25.2 2.45.57 3.6a1 1 0 0 1-.25 1z"/></svg>Fax.+1 (234) 567-8920</div>
  <div class="c-line" style="top:346px"><svg width="18" height="14" viewBox="0 0 18 14"><rect x="1" y="1" width="16" height="12" rx="1" fill="none" stroke="#e29e0c" stroke-width="2"/><path d="M1 2l8 6 8-6" fill="none" stroke="#e29e0c" stroke-width="2"/></svg>info@domainname.com</div>
  <div class="form">
    <label style="left:535px;top:172px">Name</label>
    <div class="field" style="left:535px;top:193px;width:271px;height:36px"></div>
    <label style="left:818px;top:172px">Company Name</label>
    <div class="field" style="left:818px;top:193px;width:271px;height:36px"></div>
    <label style="left:535px;top:241px">Your Email</label>
    <div class="field" style="left:535px;top:262px;width:271px;height:36px"></div>
    <label style="left:818px;top:241px">Your Phone</label>
    <div class="field" style="left:818px;top:262px;width:271px;height:36px"></div>
    <label style="left:535px;top:309px">How Can We Help?</label>
    <div class="field" style="left:535px;top:330px;width:554px;height:80px"></div>
    <span class="btn">Submit now</span>
  </div>
</section>

<footer class="site-footer">
  <div class="f-brand"><span class="dot"></span>KEELSTONE 3PL</div>
  <div class="social"><span></span><span></span><span></span></div>
  <h4 style="left:456px">Links</h4>
  <ul class="f-links" style="left:456px"><li>Home</li><li>Who we are</li><li>Why use a prep 3PL?</li><li>Benefits</li></ul>
  <ul class="f-links" style="left:679px"><li>Our Software</li><li>Terms of Use</li><li>Privacy Policy</li><li>Contact Us</li></ul>
  <h4 style="left:878px">Contact details</h4>
  <div class="f-contact">
    <div><svg width="10" height="14" viewBox="0 0 10 14"><path fill="#fff" d="M5 0a5 5 0 0 1 5 5c0 4-5 9-5 9S0 9 0 5a5 5 0 0 1 5-5zm0 3a2 2 0 1 0 0 4 2 2 0 0 0 0-4z"/></svg><span>123 KEELSTONE 3PL, City Name,<br>Country Code - 11580</span></div>
    <div><svg width="14" height="12" viewBox="0 0 18 14"><rect x="1" y="1" width="16" height="12" fill="none" stroke="#fff" stroke-width="2"/><path d="M1 2l8 6 8-6" fill="none" stroke="#fff" stroke-width="2"/></svg>info@domainname.com</div>
    <div><svg width="12" height="12" viewBox="0 0 24 24"><path fill="#fff" d="M6.6 10.8a15 15 0 0 0 6.6 6.6l2.2-2.2a1 1 0 0 1 1-.25 11.4 11.4 0 0 0 3.6.57 1 1 0 0 1 1 1V20a1 1 0 0 1-1 1A17 17 0 0 1 3 4a1 1 0 0 1 1-1h3.5a1 1 0 0 1 1 1c0 1.25.2 2.45.57 3.6a1 1 0 0 1-.25 1z"/></svg><b>+1 (234) 567-8900</b></div>
  </div>
  <div class="rule"></div>
  <div class="copy">Copyright © 2021 KEELSTONE 3PL. All rights reserved</div>
</footer>

<section class="disclaimer">
  <h5>Disclaimer</h5>
  <p>*Our guarantee is 48 hours from the time an outbound shipment is created in our system. Weekends and holidays excluded. Orders created on a Friday after hours, Saturday or Sunday will be counted from the open of business on Monday morning. We offer a credit of up to 500 units on your next shipment. These credits are for standard prep items only, no bundles, bubble wrapped or multipack units. Outbound shipments will be prepped and ready to ship. We are unable to control shipping companies and freight carriers. Orders after daily pickups are completed will be ready for next day pickup.</p>
</section>

</body>
</html>
```